Landing Page Design für Ankauf von Edelmetallen
Zielgruppe
Ankauf von Edelmetallen über einen Onlineshop, alle Altersgruppen ab 18 Jahre!
Aufgabenstellung
Website: flinkmetall.de
Aufgabenstellung:
Mit unserer Ankaufsplattform (flinkmetall.de) werden derzeit keine Verkäufe erzeugt, wir denken das es an der Landingpage liegt, daher soll eine neue Landingpage designt werden.
Ziel ist es eine Landingpage (Ladenbau 5) zu designen die Vertrauen und absolute Seriösität vermittelt.
Beim Verkauf von Edelmetallen übers Internet muss der Kunde sich gut aufgehoben fühlen.
Beispiele für erfolgreiche Ankaufsplattformen sind: silbertaler.de, Wertankauf789.de, Metall7schnell.de,
Zwingende Vorgaben:
-Die jetzige Menüleiste ist nicht veränderbar, dies liegt an dem starren CMS von Ladenbau
-Unsere Ankaufspreise für Gold & Silber (Tabellenform) sollen dem Kunden beim besuch der Seite direkt ins Auge springen.
-Der Kunde soll zwischen zwei Verkaufswegen entscheiden können: Direktverkauf oder Versandtasche.
- USPs sollen im Header dargestellt werden können
- Schritt für Schritt Anleitung für beide Verkaufswege: Direktverkauf & Versandtasche
- freie Farbgestaltung
Dateiformat: Photoshop (PSD-Datei)
responsive Design (Desktop, Tablet, Smartphone)

```html
<!DOCTYPE html>
<html lang="de">
<head>
<meta charset="utf-8">
<title>flinkmetall.de – Landingpage Ankauf Edelmetalle</title>
<link href="https://fonts.googleapis.com/css2?family=Playfair+Display:wght@500;600;700&family=Poppins:wght@400;500;600;700&display=swap" rel="stylesheet">
<style>
:root{
  --board-top:#3c3c3c;
  --board-bottom:#000;
  --gold:#d5b03b;
  --gold-dark:#c39d2c;
  --gold-text:#c9a134;
  --ink:#222;
  --ink-soft:#666;
  --rule:#e2cf8c;
  --panel-top:#2d2514;
  --panel-bottom:#18130a;
  --bar:#2b2b2b;
  --footer-grey:#eef0f3;
  --white:#fff;
}
*{box-sizing:border-box;margin:0;padding:0}
html,body{width:1200px;height:2212px;overflow:hidden;background:#000}
body{font-family:"Poppins",sans-serif;color:var(--ink)}
.board{position:absolute;left:0;top:0;width:1400px;height:2580px;transform:scale(.857143);transform-origin:0 0;
  background:linear-gradient(180deg,var(--board-top) 0,#2e2e2e 700px,#111 1700px,var(--board-bottom) 100%)}
.abs{position:absolute}
.board__label{position:absolute;top:74px;color:#fff;font:500 15px "Poppins",sans-serif}
.board__rule{position:absolute;left:78px;top:106px;width:1217px;height:1px;background:#bdbdbd}
.screen{position:absolute;background:#fff;overflow:hidden}
.serif{font-family:"Playfair Display",serif;font-weight:600;color:var(--ink);line-height:1.15}
.gold{color:var(--gold-text)}
.eyebrow{position:absolute;color:var(--gold-text);font-weight:500;letter-spacing:.08em;text-transform:uppercase}
.copy{position:absolute;color:var(--ink-soft);line-height:1.75}
.btn{position:absolute;display:flex;align-items:center;justify-content:center;font-weight:600;text-transform:uppercase;letter-spacing:.02em;text-align:center}
.btn--gold{background:var(--gold);color:var(--ink);box-shadow:0 1px 2px rgba(0,0,0,.25)}
.btn--dark{background:#2a2a2a;color:#fff}
.btn--outline{border:1px solid #fff;color:#fff}
.topbar{position:absolute;left:0;top:0;width:100%;background:var(--bar);color:#fff}
.navbar{position:absolute;left:0;width:100%;background:var(--gold);color:#fff}
.usp{position:absolute;left:0;width:100%;background:var(--gold-dark);color:#2b2410}
.logo{position:absolute;display:flex;align-items:center;color:#fff;font-weight:700}
.logo__dot{border-radius:50%;background:#fff;margin-right:3px}
.hero{position:absolute;left:0;width:100%;
  background:radial-gradient(ellipse 40% 45% at 72% 42%,rgba(214,170,60,.75),rgba(150,110,30,.35) 45%,transparent 75%),
  radial-gradient(ellipse 30% 30% at 85% 20%,rgba(230,200,160,.35),transparent 70%),
  linear-gradient(135deg,#3a3123 0,#241d13 45%,#2f271a 70%,#1b160e 100%)}
.hero__title{position:absolute;color:#fff;font-family:"Playfair Display",serif;font-weight:600;line-height:1.12}
.hero__list{position:absolute;list-style:none;color:#fff;white-space:nowrap}
.hero__list li{position:relative}
.hero__list li::before{content:"";position:absolute;border-radius:50%;background:var(--gold)}
.screen--desktop .hero__list li::before{left:0;top:5px;width:5px;height:5px}
.screen--tablet .hero__list li::before{left:0;top:3px;width:3px;height:3px}
.screen--mobile .hero__list li::before{left:0;top:1.5px;width:2.5px;height:2.5px}
.seal{position:absolute;border-radius:50%;background:radial-gradient(circle,#e6c55a 0,#c99e2b 62%,#8a6a17 64%,#d9b646 70%,#b88e23 100%)}
.price-card{position:absolute;background:#fff;box-shadow:0 2px 6px rgba(0,0,0,.18);text-align:center}
.price-card__title{font-weight:700;color:var(--ink);letter-spacing:.03em}
.price-card__meta{color:var(--ink-soft)}
.price-table{position:absolute;border-collapse:collapse;color:var(--ink)}
.price-table td{border-bottom:1px solid var(--rule);text-align:left}
.price-table td:last-child{text-align:right;font-weight:600}
.price-card__note{position:absolute;color:var(--ink-soft)}
.cat-card{position:absolute;background:#fff;box-shadow:0 1px 4px rgba(0,0,0,.2);text-align:center}
.cat-card__img{position:absolute;left:50%;transform:translateX(-50%);border-radius:50%}
.cat-card__img--gold{background:radial-gradient(circle at 40% 35%,#f6de7c,#d9ad2c 60%,#a97d14)}
.cat-card__img--silver{background:radial-gradient(circle at 40% 35%,#f4f4f4,#b9b9b9 60%,#7f7f7f)}
.cat-card__img--cutlery{border-radius:4px;background:linear-gradient(90deg,transparent 0,#d8cfc6 30%,#b9a89a 50%,#d8cfc6 70%,transparent 100%)}
.cat-card__title{position:absolute;left:0;width:100%;font-family:"Playfair Display",serif;font-weight:600;color:var(--ink)}
.cat-card__sub{position:absolute;left:0;width:100%;color:var(--gold-text)}
.steps{position:absolute;left:0;top:0;width:205px;height:448px;background:linear-gradient(160deg,var(--panel-top),var(--panel-bottom));color:#fff;transform-origin:0 0}
.steps__head{height:32px;background:var(--gold);display:flex;align-items:center;justify-content:center;font-weight:700;font-size:10px;letter-spacing:.12em}
.steps__intro{position:absolute;left:22px;top:42px;width:161px;font-size:6px;line-height:1.5;text-align:center}
.steps__num{position:absolute;left:40px;font-family:"Playfair Display",serif;font-size:20px;font-weight:600}
.steps__line{position:absolute;left:50px;width:1px;background:rgba(255,255,255,.7)}
.steps__icon{position:absolute;left:69px;width:24px;height:22px;stroke:var(--gold);fill:none;stroke-width:1.3}
.steps__text{position:absolute;left:69px;width:125px;font-size:6.2px;font-weight:600;line-height:1.4;text-transform:uppercase}
.steps__btn{left:45px;top:414px;width:112px;height:22px;font-size:6px}
.photo{position:absolute}
.photo--expert{background:radial-gradient(ellipse 45% 55% at 45% 45%,#8a7a66,#4a3e30 55%,#231c14 100%)}
.review{position:absolute;background:#fff;box-shadow:0 1px 5px rgba(0,0,0,.2);text-align:center}
.review__stars{color:var(--gold);letter-spacing:.25em}
.review__text{font-family:"Playfair Display",serif;font-style:italic;color:#666;line-height:1.7}
.review__name{font-weight:600;color:var(--ink)}
.review-badge{position:absolute;border-radius:50%;background:radial-gradient(circle,#fff 0,#fff 55%,#d6b03d 58%,#b88e23 100%);box-shadow:0 1px 2px rgba(0,0,0,.3)}
.arrow{position:absolute;background:var(--gold);display:flex;align-items:center;justify-content:center}
.arrow svg{stroke:#fff;fill:none;stroke-width:2}
.cta{position:absolute;left:0;width:100%;background:linear-gradient(180deg,#d8b444,#c9a332);text-align:center}
.cta__title{position:absolute;left:0;width:100%;color:#fff;font-family:"Playfair Display",serif;font-weight:600}
.foot-h{position:absolute;font-weight:500;color:var(--ink)}
.foot-t{position:absolute;color:#555;line-height:1.65}
.foot-bottom{position:absolute;left:0;width:100%;background:var(--footer-grey);text-align:center;color:#555}
.social{display:inline-block;border-radius:50%}
.social--blue{background:#3b5bab}
.social--green{background:#37b24d}
.pay{position:absolute;background:#e9ecd9}
.ship{position:absolute;background:#f0c419}
.to-top{position:absolute;background:#333}
.link-u{position:absolute;font-weight:600;color:var(--ink);border-bottom:1px solid var(--gold)}
.acc-row{position:absolute;left:0;width:100%;border-bottom:1px solid #e3e3e3;display:flex;justify-content:space-between;align-items:center;padding:0 6px;font-size:5px;color:#333}
.m-icons{position:absolute;display:flex;justify-content:space-around;width:100%;color:#fff;font-size:3px}
.m-icons span{display:flex;flex-direction:column;align-items:center;gap:1px}
.m-icons i{display:block;width:6px;height:5px;border:1px solid #fff;border-radius:1px}
</style>
</head>
<body>
<svg width="0" height="0" style="position:absolute">
  <defs>
    <symbol id="i-scale" viewBox="0 0 24 22"><path d="M12 2v18M5 20h14M4 5h16M4 5l-3 7h6zM20 5l-3 7h6z"/></symbol>
    <symbol id="i-basket" viewBox="0 0 24 22"><path d="M2 9h20l-2 11H4zM6 9l4-6M18 9l-4-6M8 12v5M12 12v5M16 12v5"/></symbol>
    <symbol id="i-mail" viewBox="0 0 24 22"><path d="M2 4h20v14H2zM2 4l10 8 10-8"/></symbol>
    <symbol id="i-cash" viewBox="0 0 24 22"><path d="M2 5h20v12H2zM5 8h14v6H5z"/><circle cx="12" cy="11" r="2"/></symbol>
    <symbol id="i-phone" viewBox="0 0 24 22"><path d="M7 1h10v20H7zM10 18h4M11 6l2 3-2 3"/></symbol>
    <symbol id="i-calc" viewBox="0 0 24 22"><path d="M4 1h16v20H4zM7 4h10v4H7zM7 11h2M11 11h2M15 11h2M7 15h2M11 15h2M15 15h2"/></symbol>
    <symbol id="i-truck" viewBox="0 0 24 22"><path d="M1 7h14v9H1zM15 10h4l3 3v3h-7M5 19a2 2 0 100-.1M18 19a2 2 0 100-.1M1 4h6"/></symbol>
  </defs>
</svg>

<div class="board">
  <div class="board__label" style="left:78px">Deskop 1920px</div>
  <div class="board__label" style="left:823px">Tablet 768px</div>
  <div class="board__label" style="left:1165px">Smartphone 360px</div>
  <div class="board__rule"></div>

  <!-- ================= DESKTOP ================= -->
  <section class="screen screen--desktop" style="left:78px;top:146px;width:664px;height:2239px">
    <div class="topbar" style="height:14px;font-size:5px">
      <span class="abs" style="left:125px;top:4px">Mein Konto ⌄</span>
      <span class="abs" style="left:170px;top:4px">Service/Hilfe ⌄</span>
      <span class="abs" style="left:220px;top:4px">⌕ Suchen</span>
      <span class="abs" style="left:489px;top:1px;width:53px;height:13px;background:#fff;color:#222;padding:3px 0 0 5px">▪ Verkaufskorb</span>
    </div>
    <div class="navbar" style="top:14px;height:26px">
      <div class="logo" style="left:127px;top:6px;font-size:7.5px"><span class="logo__dot" style="width:12px;height:12px"></span>flinkmetall.de</div>
      <div class="abs" style="left:290px;top:10px;display:flex;gap:10px;font-size:5.5px;font-weight:600">
        <span>⌂</span><span>Gold und Silber verkaufen</span><span>Versandtasche</span><span>So geht´s</span><span>Wissenswertes</span>
      </div>
    </div>
    <div class="usp" style="top:40px;height:14px;font-size:4.5px">
      <span class="abs" style="left:125px;top:4px">▲ Aktuelle börsenorientierte Preise</span>
      <span class="abs" style="left:263px;top:4px">▬ kostenloser Versand versichert bis 5000 € pro Paket</span>
      <span class="abs" style="left:437px;top:4px">⌂ 3 Tage Preisgarantie ab Verkaufsdatum</span>
    </div>
    <div class="hero" style="top:54px;height:320px" role="img" aria-label="Foto: Hand hält goldene Ketten vor dunklem Steinhintergrund"></div>
    <div class="eyebrow" style="left:125px;top:124px;font-size:6.5px">Ankauf von Gold &amp; Silber</div>
    <h1 class="hero__title" style="left:125px;top:138px;font-size:25px">Machen Sie Ihr<br><span class="gold">Gold</span> zu Geld</h1>
    <ul class="hero__list" style="left:125px;top:207px;font-size:7px;line-height:14.5px">
      <li style="padding-left:11px">Höchste Ankaufspreise</li>
      <li style="padding-left:11px">Keine Gebühren &amp; Abzüge</li>
      <li style="padding-left:11px">Sicherste &amp; diskrete Abwicklung</li>
      <li style="padding-left:11px">Kostenloser Paket-Versand</li>
    </ul>
    <a class="btn btn--gold" style="left:125px;top:279px;width:106px;height:22px;font-size:5.5px">Aktuelle Preise prüfen</a>
    <div class="seal" style="left:127px;top:322px;width:64px;height:64px" role="img" aria-label="Siegel Geld-zurück-Garantie"></div>
    <div class="seal" style="left:216px;top:322px;width:66px;height:66px" role="img" aria-label="Siegel Kundenbewertungen"></div>

    <div class="price-card" style="left:335px;top:300px;width:205px;height:234px">
      <div class="price-card__title" style="margin-top:14px;font-size:7.5px">AKTUELLE ANKAUFKURSE</div>
      <div class="price-card__meta" style="margin-top:5px;font-size:5px">Ankaufspreise Stand: 04.01.2022 / 15:45 Uhr</div>
      <div class="abs" style="left:29px;top:50px;width:147px;height:1px;background:var(--rule)"></div>
      <table class="price-table" style="left:29px;top:58px;width:139px;font-size:5.5px">
        <tr><td style="height:14.5px">999er Gold (24k)</td><td>50,49 € /g</td></tr>
        <tr><td style="height:14.5px">900er Gold (21k)</td><td>45,44 € /g</td></tr>
        <tr><td style="height:14.5px">750er Gold (18k)</td><td>37,87 € /g</td></tr>
        <tr><td style="height:14.5px">585er Gold (14k)</td><td>29,54 € /g</td></tr>
        <tr><td style="height:14.5px">999er Silber</td><td>0,60 € /g</td></tr>
        <tr><td style="height:14.5px">900er Silber</td><td>0,50 € /g</td></tr>
        <tr><td style="height:14.5px">750er Silber</td><td>0,45 € /g</td></tr>
        <tr><td style="height:14.5px">625er Silber</td><td>0,38 € /g</td></tr>
      </table>
      <div class="price-card__note" style="right:19px;top:182px;font-size:4.8px">Alle Angaben ohne Gewähr.</div>
      <a class="btn btn--gold" style="left:48px;top:198px;width:110px;height:22px;font-size:5.8px">Alle Preise anschauen</a>
    </div>

    <div class="eyebrow" style="left:128px;top:442px;font-size:6px">Ankauf von Gold &amp; Silber</div>
    <h2 class="serif abs" style="left:128px;top:455px;font-size:16.5px">Wir kaufen Ihr <span class="gold">Gold</span> &amp;<br>Silber zum Höchstpreis</h2>
    <p class="copy" style="left:128px;top:501px;width:190px;font-size:5.6px">Lorem ipsum dolor sit amet, consetetur sadipscing elitr, sed diam nonumy eirmod tempor invidunt ut labore et dolore magna aliquyam erat, sed diam voluptua. At vero</p>

    <div class="cat-card" style="left:127px;top:582px;width:131px;height:132px">
      <div class="cat-card__img cat-card__img--gold" style="top:12px;width:70px;height:70px" role="img" aria-label="Foto: Goldmünze"></div>
      <div class="cat-card__title" style="top:90px;font-size:12.5px">Gold-Ankauf</div>
      <div class="cat-card__sub" style="top:111px;font-size:6px">Barren | Münzen |Schmuck</div>
    </div>
    <div class="cat-card" style="left:269px;top:582px;width:131px;height:132px">
      <div class="cat-card__img cat-card__img--silver" style="top:12px;width:70px;height:70px" role="img" aria-label="Foto: Silbermünze"></div>
      <div class="cat-card__title" style="top:90px;font-size:12.5px">Silber-Ankauf</div>
      <div class="cat-card__sub" style="top:111px;font-size:6px">Barren | Münzen |Schmuck</div>
    </div>
    <div class="cat-card" style="left:408px;top:582px;width:131px;height:132px">
      <div class="cat-card__img cat-card__img--cutlery" style="top:12px;width:50px;height:70px" role="img" aria-label="Foto: Silberbesteck"></div>
      <div class="cat-card__title" style="top:90px;font-size:12.5px">Gemischtes</div>
      <div class="cat-card__sub" style="top:111px;font-size:6px">Besteck | Zahngold | Diverses</div>
    </div>
    <a class="btn btn--gold" style="left:279px;top:732px;width:111px;height:24px;font-size:5.5px">Jetzt Höchstpreis sichern</a>

    <div class="eyebrow" style="left:0;width:664px;text-align:center;top:790px;font-size:6px">Ankauf in nur 4 Schritten</div>
    <h2 class="serif abs" style="left:0;width:664px;text-align:center;top:800px;font-size:16.5px">Wählen Sie Ihren bevorzugten Ankaufsweg</h2>

    <div class="abs" style="left:125px;top:834px;width:205px;height:448px">
      <div class="steps">
        <div class="steps__head">DIREKTVERKAUF</div>
        <p class="steps__intro">So einfach wie im Online-Shop, nur umgekehrt.<br>Wählen Sie Ihre Gold- oder Silberart und verkaufen Sie diese direkt hier im Shop.</p>
        <svg class="steps__icon" style="top:88px"><use href="#i-scale"/></svg>
        <div class="steps__num" style="top:118px">1</div><div class="steps__text" style="top:124px">Gold &amp; Silber wählen<br>und Gewicht wiegen<br>oder schätzen</div>
        <div class="steps__line" style="top:148px;height:24px"></div>
        <svg class="steps__icon" style="top:168px"><use href="#i-basket"/></svg>
        <div class="steps__num" style="top:194px">2</div><div class="steps__text" style="top:200px">Verkaufskorb füllen<br>und Ihren Erlös<br>direkt sehen</div>
        <div class="steps__line" style="top:226px;height:24px"></div>
        <svg class="steps__icon" style="top:246px"><use href="#i-mail"/></svg>
        <div class="steps__num" style="top:274px">3</div><div class="steps__text" style="top:280px">Gold mit kostenloser<br>Versandmarke versenden<br>oder selbst anliefern</div>
        <div class="steps__line" style="top:305px;height:24px"></div>
        <svg class="steps__icon" style="top:324px"><use href="#i-cash"/></svg>
        <div class="steps__num" style="top:352px">4</div><div class="steps__text" style="top:358px">Auszahlung direkt auf<br>Ihr Konto oder bei<br>Anlieferung in bar erhalten</div>
        <a class="btn btn--gold steps__btn">Direkt verkaufen</a>
      </div>
    </div>
    <div class="abs" style="left:335px;top:834px;width:205px;height:448px">
      <div class="steps">
        <div class="steps__head">POSTVERSAND</div>
        <p class="steps__intro">Verkaufen Sie Ihr Gold bequem per Post.<br>Mit dieser Verkaufsanleitung kommen Sie schnell und sicher zu Ihrem Geld.</p>
        <svg class="steps__icon" style="top:88px"><use href="#i-phone"/></svg>
        <div class="steps__num" style="top:118px">1</div><div class="steps__text" style="top:124px">Versandtasche<br>bestellen</div>
        <div class="steps__line" style="top:148px;height:24px"></div>
        <svg class="steps__icon" style="top:168px"><use href="#i-mail"/></svg>
        <div class="steps__num" style="top:194px">2</div><div class="steps__text" style="top:200px">Gold in Versandtasche<br>legen und an uns senden</div>
        <div class="steps__line" style="top:226px;height:24px"></div>
        <svg class="steps__icon" style="top:246px"><use href="#i-calc"/></svg>
        <div class="steps__num" style="top:274px">3</div><div class="steps__text" style="top:280px">Bewertung<br>erhalten</div>
        <div class="steps__line" style="top:305px;height:24px"></div>
        <svg class="steps__icon" style="top:324px"><use href="#i-truck"/></svg>
        <div class="steps__num" style="top:352px">4</div><div class="steps__text" style="top:358px">Auszahlung<br>direkt auf Ihr Konto</div>
        <a class="btn btn--gold steps__btn">Versandtasche bestellen</a>
      </div>
    </div>

    <div class="eyebrow" style="left:126px;top:1372px;font-size:6px">Familienunternehmen mit Tradition</div>
    <h2 class="serif abs" style="left:126px;top:1384px;font-size:16.5px">Über <span class="gold">100 Jahre</span><br>Expertise in Gold</h2>
    <p class="copy" style="left:126px;top:1430px;width:195px;font-size:5.6px">Lorem ipsum dolor sit amet, consetetur sadipscing elitr, sed diam nonumy eirmod tempor invidunt ut labore et dolore magna aliquyam erat, sed diam voluptua. At vero sed diam nonumy eirmod tempor invidunt ut labore et dolore magna aliquyam erat, sed diam voluptua. At vero</p>
    <div class="link-u" style="left:126px;top:1493px;font-size:5.5px">MEHR ÜBER UNS ERFAHREN</div>
    <div class="photo photo--expert" style="left:335px;top:1349px;width:205px;height:177px" role="img" aria-label="Foto: Goldexperte prüft Schmuck mit Lupe und weißen Handschuhen"></div>

    <div class="eyebrow" style="left:0;width:664px;text-align:center;top:1608px;font-size:6px">Kundenstimmen</div>
    <h2 class="serif abs" style="left:0;width:664px;text-align:center;top:1620px;font-size:16.5px">Warum uns unsere Kunden vertrauen</h2>
    <div class="review" style="left:179px;top:1656px;width:309px;height:158px">
      <div class="review__stars" style="margin-top:20px;font-size:9px">★★★★★</div>
      <p class="review__text" style="margin:8px 14px 0;font-size:8.3px">Meine Erfahrung war einfach nur super. Total nettes Team, schneller Versand. Sehr zuverlässig. Ich bin total happy mit meinem tollen Armband. Dazu war es wundervoll verpackt mit einer kleinen persönlichen Nachricht. Ich bedanke mich!</p>
      <div class="review__name" style="margin-top:16px;font-size:5.5px">Lena Hofer</div>
    </div>
    <div class="review-badge" style="left:156px;top:1646px;width:44px;height:44px" role="img" aria-label="Siegel Kundenbewertungen"></div>
    <div class="arrow" style="left:125px;top:1724px;width:22px;height:22px"><svg width="10" height="10"><path d="M7 1L3 5l4 4"/></svg></div>
    <div class="arrow" style="left:518px;top:1719px;width:22px;height:22px"><svg width="10" height="10"><path d="M3 1l4 4-4 4"/></svg></div>

    <div class="cta" style="top:1867px;height:139px">
      <div class="cta__title" style="top:32px;font-size:17px">Wir machen Ihr Gold zu Geld.</div>
      <a class="btn btn--dark" style="left:217px;top:78px;width:112px;height:23px;font-size:5.5px">Jetzt Höchstpreise sichern</a>
      <a class="btn btn--outline" style="left:337px;top:78px;width:111px;height:23px;font-size:5.5px">Versandtasche bestellen</a>
    </div>

    <div class="foot-h" style="left:123px;top:2021px;font-size:5.5px">Über uns</div>
    <p class="foot-t" style="left:123px;top:2036px;width:200px;font-size:4.5px">Der Ankauf von Gold und weiteren Edelmetallen ist ein neues Geschäftsfeld der Firma Konrad Weller e.K. und somit Bestandteil eines alteingesessenen Familienunternehmens mit über 100-jähriger Geschichte inmitten der beschaulichen Altstadt. Ehrlichkeit, Transparenz sowie faire Konditionen sind nach unserer kaufmännischen Überzeugung der Grundstein für eine vertrauensvolle, langfristige Kundenbeziehung. <b>mehr...</b></p>
    <div class="foot-h" style="left:341px;top:2021px;font-size:5.5px">Service</div>
    <p class="foot-t" style="left:341px;top:2036px;font-size:4.5px">• So geht's<br>• Unser Angebot<br>• FAQ<br>• Über uns<br>• Großkunden</p>
    <div class="foot-h" style="left:450px;top:2021px;font-size:5.5px">Informationen</div>
    <p class="foot-t" style="left:450px;top:2036px;font-size:4.5px">• Corona-Hinweis<br>• Impressum<br>• Kontakt<br>• Privatsphäre-Einstellungen<br>• AGB<br>• Datenschutz</p>
    <div class="abs" style="left:123px;top:2029px;width:418px;height:1px;background:#eee"></div>
    <div class="foot-h" style="left:123px;top:2108px;font-size:5.5px">Kontakt</div>
    <p class="foot-t" style="left:123px;top:2124px;font-size:4.5px">Wir freuen uns auf Ihre Anfrage:<br>✉ info@flinkmetall.de<br>▪ Chatfunk-Chat</p>
    <div class="foot-h" style="left:232px;top:2108px;font-size:5.5px">Unsere Communitys</div>
    <div class="abs" style="left:232px;top:2125px;display:flex;gap:4px"><span class="social social--blue" style="width:11px;height:11px"></span><span class="social social--green" style="width:11px;height:11px"></span></div>
    <div class="foot-h" style="left:341px;top:2108px;font-size:5.5px">Auszahlungsoptionen</div>
    <div class="pay" style="left:341px;top:2127px;width:24px;height:8px"></div><div class="pay" style="left:370px;top:2127px;width:24px;height:8px"></div>
    <div class="foot-h" style="left:450px;top:2108px;font-size:5.5px">Versandoptionen</div>
    <div class="ship" style="left:450px;top:2125px;width:26px;height:11px"></div><div class="pay" style="left:481px;top:2127px;width:24px;height:8px"></div><div class="pay" style="left:510px;top:2127px;width:24px;height:8px"></div>

    <div class="foot-bottom" style="top:2171px;height:68px;font-size:4.3px">
      <div style="margin-top:9px">Kontakt | Über uns | AGB | Impressum | Datenschutz</div>
      <div style="margin-top:3px">* Bei den veröffentlichten Ankaufspreisen handelt es sich um Nettopreise.</div>
      <div style="margin-top:9px">© 2022 flinkmetall.de - All Rights Reserved. Theme by Formwerk®</div>
    </div>
    <div class="to-top" style="left:642px;top:2209px;width:14px;height:14px"><svg width="14" height="14" style="stroke:#fff;fill:none;stroke-width:1.5"><path d="M4 9l3-3 3 3"/></svg></div>
  </section>

  <!-- ================= TABLET ================= -->
  <section class="screen screen--tablet" style="left:823px;top:146px;width:266px;height:1374px">
    <div class="topbar" style="height:14px;font-size:4px">
      <span class="abs" style="left:19px;top:5px">Mein Konto ⌄</span>
      <span class="abs" style="left:74px;top:5px">⌕ Suchen</span>
      <span class="abs" style="left:171px;top:1px;width:53px;height:13px;background:#fff;color:#222;padding:4px 0 0 5px">▪ Verkaufskorb</span>
    </div>
    <div class="navbar" style="top:14px;height:26px">
      <div class="logo" style="left:95px;top:8px;font-size:6px"><span class="logo__dot" style="width:10px;height:10px"></span>flinkmetall.de</div>
    </div>
    <div class="usp" style="top:40px;height:15px;font-size:4.8px;color:#fff;font-weight:600;background:var(--gold)">
      <div class="abs" style="left:8px;top:5px;display:flex;gap:9px;white-space:nowrap"><span>⌂</span><span>Gold und Silber verkaufen</span><span>Versandtasche</span><span>So geht´s</span><span>Wissenswertes</span></div>
    </div>
    <div class="hero" style="top:55px;height:167px" role="img" aria-label="Foto: Hand hält goldene Ketten vor dunklem Steinhintergrund"></div>
    <div class="eyebrow" style="left:11px;top:66px;font-size:4px">Ankauf von Gold &amp; Silber</div>
    <div class="hero__title" style="left:11px;top:75px;font-size:12.5px">Machen Sie Ihr<br><span class="gold">Gold</span> zu Geld</div>
    <ul class="hero__list" style="left:11px;top:114px;font-size:4.3px;line-height:9.8px">
      <li style="padding-left:8px">Höchste Ankaufspreise</li>
      <li style="padding-left:8px">Keine Gebühren &amp; Abzüge</li>
      <li style="padding-left:8px">Sicherste &amp; diskrete Abwicklung</li>
      <li style="padding-left:8px">Kostenloser Paket-Versand</li>
    </ul>
    <a class="btn btn--gold" style="left:11px;top:166px;width:86px;height:17px;font-size:4px">Aktuelle Preise prüfen</a>
    <div class="seal" style="left:13px;top:196px;width:30px;height:30px" role="img" aria-label="Siegel Geld-zurück-Garantie"></div>
    <div class="seal" style="left:48px;top:196px;width:30px;height:30px" role="img" aria-label="Siegel Kundenbewertungen"></div>

    <div class="price-card" style="left:135px;top:188px;width:119px;height:124px">
      <div class="price-card__title" style="margin-top:6px;font-size:5px">AKTUELLE ANKAUFKURSE</div>
      <div class="price-card__meta" style="margin-top:1px;font-size:3.3px">Ankaufspreise Stand: 04.01.2022 / 15:45 Uhr</div>
      <table class="price-table" style="left:14px;top:26px;width:91px;font-size:3.4px">
        <tr><td style="height:8.4px">999er Gold (24k)</td><td>50,49 € /g</td></tr>
        <tr><td style="height:8.4px">900er Gold (21k)</td><td>45,44 € /g</td></tr>
        <tr><td style="height:8.4px">750er Gold (18k)</td><td>37,87 € /g</td></tr>
        <tr><td style="height:8.4px">585er Gold (14k)</td><td>29,54 € /g</td></tr>
        <tr><td style="height:8.4px">999er Silber</td><td>0,60 € /g</td></tr>
        <tr><td style="height:8.4px">900er Silber</td><td>0,50 € /g</td></tr>
        <tr><td style="height:8.4px">750er Silber</td><td>0,45 € /g</td></tr>
        <tr><td style="height:8.4px">625er Silber</td><td>0,38 € /g</td></tr>
      </table>
      <div class="price-card__note" style="left:0;width:100%;top:97px;font-size:3.2px">Alle Angaben ohne Gewähr.</div>
      <a class="btn btn--gold" style="left:29px;top:106px;width:61px;height:10px;font-size:3px">Alle Preise anschauen</a>
    </div>

    <div class="eyebrow" style="left:11px;top:250px;font-size:3.6px">Ankauf von Gold &amp; Silber</div>
    <div class="serif abs" style="left:11px;top:257px;font-size:8.5px">Wir kaufen Ihr <span class="gold">Gold</span> &amp;<br>Silber zum Höchstpreis</div>
    <p class="copy" style="left:11px;top:284px;width:112px;font-size:3.4px;line-height:1.6">Lorem ipsum dolor sit amet, consetetur sadipscing elitr, sed diam nonumy eirmod tempor invidunt ut labore et dolore magna aliquyam erat, sed diam voluptua. At vero</p>

    <div class="cat-card" style="left:10px;top:347px;width:78px;height:83px">
      <div class="cat-card__img cat-card__img--gold" style="top:8px;width:42px;height:42px" role="img" aria-label="Foto: Goldmünze"></div>
      <div class="cat-card__title" style="top:56px;font-size:7px">Gold-Ankauf</div>
      <div class="cat-card__sub" style="top:69px;font-size:3.2px">Barren | Münzen |Schmuck</div>
    </div>
    <div class="cat-card" style="left:93px;top:347px;width:78px;height:83px">
      <div class="cat-card__img cat-card__img--silver" style="top:8px;width:42px;height:42px" role="img" aria-label="Foto: Silbermünze"></div>
      <div class="cat-card__title" style="top:56px;font-size:7px">Silber-Ankauf</div>
      <div class="cat-card__sub" style="top:69px;font-size:3.2px">Barren | Münzen |Schmuck</div>
    </div>
    <div class="cat-card" style="left:176px;top:347px;width:78px;height:83px">
      <div class="cat-card__img cat-card__img--cutlery" style="top:8px;width:30px;height:42px" role="img" aria-label="Foto: Silberbesteck"></div>
      <div class="cat-card__title" style="top:56px;font-size:7px">Gemischtes</div>
      <div class="cat-card__sub" style="top:69px;font-size:3.2px">Besteck | Zahngold | Diverses</div>
    </div>
    <a class="btn btn--gold" style="left:88px;top:442px;width:90px;height:15px;font-size:3.5px">Jetzt Höchstpreis sichern</a>

    <div class="eyebrow" style="left:0;width:266px;text-align:center;top:484px;font-size:3.6px">Ankauf in nur 4 Schritten</div>
    <div class="serif abs" style="left:0;width:266px;text-align:center;top:493px;font-size:8.5px">Wählen Sie Ihren bevorzugten Ankaufsweg</div>

    <div class="abs" style="left:10px;top:518px;width:119px;height:261px;overflow:hidden">
      <div class="steps" style="transform:scale(.5805,.5826)">
        <div class="steps__head">DIREKTVERKAUF</div>
        <p class="steps__intro">So einfach wie im Online-Shop, nur umgekehrt.<br>Wählen Sie Ihre Gold- oder Silberart und verkaufen Sie diese direkt hier im Shop.</p>
        <svg class="steps__icon" style="top:88px"><use href="#i-scale"/></svg>
        <div class="steps__num" style="top:118px">1</div><div class="steps__text" style="top:124px">Gold &amp; Silber wählen<br>und Gewicht wiegen<br>oder schätzen</div>
        <div class="steps__line" style="top:148px;height:24px"></div>
        <svg class="steps__icon" style="top:168px"><use href="#i-basket"/></svg>
        <div class="steps__num" style="top:194px">2</div><div class="steps__text" style="top:200px">Verkaufskorb füllen<br>und Ihren Erlös<br>direkt sehen</div>
        <div class="steps__line" style="top:226px;height:24px"></div>
        <svg class="steps__icon" style="top:246px"><use href="#i-mail"/></svg>
        <div class="steps__num" style="top:274px">3</div><div class="steps__text" style="top:280px">Gold mit kostenloser<br>Versandmarke versenden<br>oder selbst anliefern</div>
        <div class="steps__line" style="top:305px;height:24px"></div>
        <svg class="steps__icon" style="top:324px"><use href="#i-cash"/></svg>
        <div class="steps__num" style="top:352px">4</div><div class="steps__text" style="top:358px">Auszahlung direkt auf<br>Ihr Konto oder bei<br>Anlieferung in bar erhalten</div>
        <a class="btn btn--gold steps__btn">Direkt verkaufen</a>
      </div>
    </div>
    <div class="abs" style="left:135px;top:518px;width:119px;height:261px;overflow:hidden">
      <div class="steps" style="transform:scale(.5805,.5826)">
        <div class="steps__head">POSTVERSAND</div>
        <p class="steps__intro">Verkaufen Sie Ihr Gold bequem per Post.<br>Mit dieser Verkaufsanleitung kommen Sie schnell und sicher zu Ihrem Geld.</p>
        <svg class="steps__icon" style="top:88px"><use href="#i-phone"/></svg>
        <div class="steps__num" style="top:118px">1</div><div class="steps__text" style="top:124px">Versandtasche<br>bestellen</div>
        <div class="steps__line" style="top:148px;height:24px"></div>
        <svg class="steps__icon" style="top:168px"><use href="#i-mail"/></svg>
        <div class="steps__num" style="top:194px">2</div><div class="steps__text" style="top:200px">Gold in Versandtasche<br>legen und an uns senden</div>
        <div class="steps__line" style="top:226px;height:24px"></div>
        <svg class="steps__icon" style="top:246px"><use href="#i-calc"/></svg>
        <div class="steps__num" style="top:274px">3</div><div class="steps__text" style="top:280px">Bewertung<br>erhalten</div>
        <div class="steps__line" style="top:305px;height:24px"></div>
        <svg class="steps__icon" style="top:324px"><use href="#i-truck"/></svg>
        <div class="steps__num" style="top:352px">4</div><div class="steps__text" style="top:358px">Auszahlung<br>direkt auf Ihr Konto</div>
        <a class="btn btn--gold steps__btn">Versandtasche bestellen</a>
      </div>
    </div>

    <div class="eyebrow" style="left:20px;top:811px;font-size:3.6px">Familienunternehmen mit Tradition</div>
    <div class="serif abs" style="left:20px;top:819px;font-size:8.5px">Über <span class="gold">100 Jahre</span><br>Expertise in Gold</div>
    <p class="copy" style="left:20px;top:845px;width:112px;font-size:3.4px;line-height:1.6">Lorem ipsum dolor sit amet, consetetur sadipscing elitr, sed diam nonumy eirmod tempor invidunt ut labore et dolore magna aliquyam erat, sed diam voluptua. At vero sed diam nonumy eirmod tempor invidunt ut labore et dolore magna aliquyam erat.</p>
    <div class="link-u" style="left:20px;top:886px;font-size:3.4px">MEHR ÜBER UNS ERFAHREN</div>
    <div class="photo photo--expert" style="left:135px;top:811px;width:119px;height:103px" role="img" aria-label="Foto: Goldexperte prüft Schmuck mit Lupe"></div>

    <div class="eyebrow" style="left:0;width:266px;text-align:center;top:935px;font-size:3.6px">Kundenstimmen</div>
    <div class="serif abs" style="left:0;width:266px;text-align:center;top:943px;font-size:7.5px">Warum uns unsere Kunden vertrauen</div>
    <div class="review" style="left:42px;top:979px;width:182px;height:92px">
      <div class="review__stars" style="margin-top:10px;font-size:5px">★★★★★</div>
      <p class="review__text" style="margin:5px 14px 0;font-size:4.6px">Meine Erfahrung war einfach nur super. Total nettes Team, schneller Versand. Sehr zuverlässig. Ich bin total happy mit meinem tollen Armband. Dazu war es wundervoll verpackt mit einer kleinen persönlichen Nachricht. Ich bedanke mich!</p>
      <div class="review__name" style="margin-top:8px;font-size:3.3px">Lena Hofer</div>
    </div>
    <div class="review-badge" style="left:47px;top:966px;width:24px;height:24px" role="img" aria-label="Siegel Kundenbewertungen"></div>
    <div class="arrow" style="left:10px;top:1020px;width:11px;height:11px"><svg width="6" height="6"><path d="M4 1L2 3l2 2"/></svg></div>
    <div class="arrow" style="left:244px;top:1020px;width:11px;height:11px"><svg width="6" height="6"><path d="M2 1l2 2-2 2"/></svg></div>

    <div class="cta" style="top:1101px;height:84px">
      <div class="cta__title" style="top:12px;font-size:8.5px">Wir machen Ihr Gold zu Geld.</div>
      <a class="btn btn--dark" style="left:34px;top:44px;width:90px;height:15px;font-size:3.3px">Jetzt Höchstpreise sichern</a>
      <a class="btn btn--outline" style="left:142px;top:44px;width:89px;height:15px;font-size:3.3px">Versandtasche bestellen</a>
    </div>

    <div class="foot-h" style="left:10px;top:1198px;font-size:4px">Kontakt</div>
    <p class="foot-t" style="left:10px;top:1210px;font-size:3.3px">Wir freuen uns auf<br>Ihre Anfrage:<br>✉<br>info@flinkmetall.de<br>▪ Chatfunk-Chat</p>
    <div class="foot-h" style="left:75px;top:1198px;font-size:4px">Service</div>
    <p class="foot-t" style="left:75px;top:1210px;font-size:3.3px">• So geht's<br>• Unser Angebot<br>• FAQ<br>• Über uns<br>• Großkunden</p>
    <div class="foot-h" style="left:141px;top:1198px;font-size:4px">Informationen</div>
    <p class="foot-t" style="left:141px;top:1210px;font-size:3.3px">• Corona-Hinweis<br>• Impressum<br>• Kontakt<br>• Privatsphäre-<br>&nbsp; Einstellungen<br>• AGB<br>• Datenschutz</p>
    <div class="foot-h" style="left:207px;top:1198px;font-size:4px">Zahlung &amp; Versand</div>
    <div class="pay" style="left:207px;top:1212px;width:16px;height:5px"></div><div class="pay" style="left:226px;top:1212px;width:16px;height:5px"></div><div class="ship" style="left:244px;top:1211px;width:12px;height:6px"></div>
    <div class="pay" style="left:207px;top:1221px;width:16px;height:5px"></div><div class="pay" style="left:226px;top:1221px;width:16px;height:5px"></div>

    <div class="foot-bottom" style="top:1284px;height:90px;font-size:3.3px">
      <div style="margin-top:10px;display:flex;justify-content:center;gap:4px"><span class="social social--blue" style="width:11px;height:11px"></span><span class="social social--green" style="width:11px;height:11px"></span></div>
      <div style="margin-top:6px">Kontakt | Über uns | AGB | Impressum | Datenschutz</div>
      <div style="margin-top:2px">* Bei den veröffentlichten Ankaufspreisen handelt es sich um Nettopreise.</div>
      <div style="margin-top:7px">© 2022 flinkmetall.de - All Rights Reserved. Theme by Formwerk®</div>
    </div>
  </section>

  <!-- ================= SMARTPHONE ================= -->
  <section class="screen screen--mobile" style="left:1170px;top:146px;width:125px;height:1926px">
    <div class="navbar" style="top:0;height:19px">
      <div class="logo" style="left:36px;top:5px;font-size:5px"><span class="logo__dot" style="width:8px;height:8px"></span>flinkmetall.de</div>
    </div>
    <div class="navbar" style="top:19px;height:23px">
      <div class="m-icons" style="top:5px">
        <span><i></i>Menü</span><span><i style="border-radius:50%"></i>Suchen</span><span><i style="border-radius:50%"></i>Mein Konto</span><span><i></i>Verkaufskorb</span>
      </div>
    </div>
    <div class="usp" style="top:42px;height:9px;font-size:2.8px;color:#fff;background:#2f2a1e">
      <span class="abs" style="left:6px;top:3px">▬ kostenloser Versand versichert bis 5000 € pro Paket</span>
    </div>
    <div class="hero" style="top:51px;height:139px" role="img" aria-label="Foto: Hand hält goldene Ketten vor dunklem Steinhintergrund"></div>
    <div class="eyebrow" style="left:8px;top:78px;font-size:2.8px">Ankauf von Gold &amp; Silber</div>
    <div class="hero__title" style="left:8px;top:85px;font-size:7.5px">Machen Sie Ihr<br><span class="gold">Gold</span> zu Geld</div>
    <ul class="hero__list" style="left:8px;top:112px;font-size:3px;line-height:6.3px">
      <li style="padding-left:5px">Höchste Ankaufspreise</li>
      <li style="padding-left:5px">Keine Gebühren &amp; Abzüge</li>
      <li style="padding-left:5px">Sicherste &amp; diskrete Abwicklung</li>
      <li style="padding-left:5px">Kostenloser Paket-Versand</li>
    </ul>
    <a class="btn btn--gold" style="left:8px;top:148px;width:61px;height:11px;font-size:2.7px">Aktuelle Preise prüfen</a>
    <div class="seal" style="left:9px;top:170px;width:20px;height:20px" role="img" aria-label="Siegel Geld-zurück-Garantie"></div>
    <div class="seal" style="left:38px;top:170px;width:20px;height:20px" role="img" aria-label="Siegel Kundenbewertungen"></div>

    <div class="eyebrow" style="left:8px;top:212px;font-size:2.8px">Ankauf von Gold &amp; Silber</div>
    <div class="serif abs" style="left:8px;top:219px;font-size:7.2px">Wir kaufen Ihr <span class="gold">Gold</span> &amp;<br>Silber zum Höchstpreis</div>
    <p class="copy" style="left:8px;top:242px;width:108px;font-size:2.7px;line-height:1.6">Lorem ipsum dolor sit amet, consetetur sadipscing elitr, sed diam nonumy eirmod tempor invidunt ut labore et dolore magna aliquyam erat, sed diam voluptua. At vero</p>

    <div class="price-card" style="left:8px;top:268px;width:109px;height:126px">
      <div class="price-card__title" style="margin-top:6px;font-size:4.5px">AKTUELLE ANKAUFKURSE</div>
      <div class="price-card__meta" style="margin-top:1px;font-size:3px">Ankaufspreise Stand: 04.01.2022 / 15:45 Uhr</div>
      <table class="price-table" style="left:12px;top:25px;width:85px;font-size:3.2px">
        <tr><td style="height:8.6px">999er Gold (24k)</td><td>50,49 € /g</td></tr>
        <tr><td style="height:8.6px">900er Gold (21k)</td><td>45,44 € /g</td></tr>
        <tr><td style="height:8.6px">750er Gold (18k)</td><td>37,87 € /g</td></tr>
        <tr><td style="height:8.6px">585er Gold (14k)</td><td>29,54 € /g</td></tr>
        <tr><td style="height:8.6px">999er Silber</td><td>0,60 € /g</td></tr>
        <tr><td style="height:8.6px">900er Silber</td><td>0,50 € /g</td></tr>
        <tr><td style="height:8.6px">750er Silber</td><td>0,45 € /g</td></tr>
        <tr><td style="height:8.6px">625er Silber</td><td>0,38 € /g</td></tr>
      </table>
      <div class="price-card__note" style="left:0;width:100%;top:98px;font-size:3px">Alle Angaben ohne Gewähr.</div>
      <a class="btn btn--gold" style="left:24px;top:108px;width:61px;height:10px;font-size:2.8px">Alle Preise anschauen</a>
    </div>

    <div class="cat-card" style="left:21px;top:413px;width:82px;height:83px">
      <div class="cat-card__img cat-card__img--gold" style="top:8px;width:42px;height:42px" role="img" aria-label="Foto: Goldmünze"></div>
      <div class="cat-card__title" style="top:56px;font-size:6.5px">Gold-Ankauf</div>
      <div class="cat-card__sub" style="top:69px;font-size:3px">Barren | Münzen |Schmuck</div>
    </div>
    <div class="cat-card" style="left:21px;top:506px;width:82px;height:83px">
      <div class="cat-card__img cat-card__img--silver" style="top:8px;width:42px;height:42px" role="img" aria-label="Foto: Silbermünze"></div>
      <div class="cat-card__title" style="top:56px;font-size:6.5px">Silber-Ankauf</div>
      <div class="cat-card__sub" style="top:69px;font-size:3px">Barren | Münzen |Schmuck</div>
    </div>
    <div class="cat-card" style="left:21px;top:599px;width:82px;height:83px">
      <div class="cat-card__img cat-card__img--cutlery" style="top:8px;width:30px;height:42px" role="img" aria-label="Foto: Silberbesteck"></div>
      <div class="cat-card__title" style="top:56px;font-size:6.5px">Gemischtes</div>
      <div class="cat-card__sub" style="top:69px;font-size:3px">Besteck | Zahngold | Diverses</div>
    </div>
    <a class="btn btn--gold" style="left:31px;top:700px;width:62px;height:11px;font-size:2.7px">Jetzt Höchstpreis sichern</a>

    <div class="eyebrow" style="left:0;width:125px;text-align:center;top:730px;font-size:2.8px">Ankauf in nur 4 Schritten</div>
    <div class="serif abs" style="left:0;width:125px;text-align:center;top:737px;font-size:7px">Wählen Sie Ihren<br>bevorzugten Ankaufsweg</div>

    <div class="abs" style="left:8px;top:772px;width:109px;height:240px;overflow:hidden">
      <div class="steps" style="transform:scale(.5317,.5357)">
        <div class="steps__head">DIREKTVERKAUF</div>
        <p class="steps__intro">So einfach wie im Online-Shop, nur umgekehrt.<br>Wählen Sie Ihre Gold- oder Silberart und verkaufen Sie diese direkt hier im Shop.</p>
        <svg class="steps__icon" style="top:88px"><use href="#i-scale"/></svg>
        <div class="steps__num" style="top:118px">1</div><div class="steps__text" style="top:124px">Gold &amp; Silber wählen<br>und Gewicht wiegen<br>oder schätzen</div>
        <div class="steps__line" style="top:148px;height:24px"></div>
        <svg class="steps__icon" style="top:168px"><use href="#i-basket"/></svg>
        <div class="steps__num" style="top:194px">2</div><div class="steps__text" style="top:200px">Verkaufskorb füllen<br>und Ihren Erlös<br>direkt sehen</div>
        <div class="steps__line" style="top:226px;height:24px"></div>
        <svg class="steps__icon" style="top:246px"><use href="#i-mail"/></svg>
        <div class="steps__num" style="top:274px">3</div><div class="steps__text" style="top:280px">Gold mit kostenloser<br>Versandmarke versenden<br>oder selbst anliefern</div>
        <div class="steps__line" style="top:305px;height:24px"></div>
        <svg class="steps__icon" style="top:324px"><use href="#i-cash"/></svg>
        <div class="steps__num" style="top:352px">4</div><div class="steps__text" style="top:358px">Auszahlung direkt auf<br>Ihr Konto oder bei<br>Anlieferung in bar erhalten</div>
        <a class="btn btn--gold steps__btn">Direkt verkaufen</a>
      </div>
    </div>
    <div class="abs" style="left:8px;top:1024px;width:109px;height:242px;overflow:hidden">
      <div class="steps" style="transform:scale(.5317,.5402)">
        <div class="steps__head">POSTVERSAND</div>
        <p class="steps__intro">Verkaufen Sie Ihr Gold bequem per Post.<br>Mit dieser Verkaufsanleitung kommen Sie schnell und sicher zu Ihrem Geld.</p>
        <svg class="steps__icon" style="top:88px"><use href="#i-phone"/></svg>
        <div class="steps__num" style="top:118px">1</div><div class="steps__text" style="top:124px">Versandtasche<br>bestellen</div>
        <div class="steps__line" style="top:148px;height:24px"></div>
        <svg class="steps__icon" style="top:168px"><use href="#i-mail"/></svg>
        <div class="steps__num" style="top:194px">2</div><div class="steps__text" style="top:200px">Gold in Versandtasche<br>legen und an uns senden</div>
        <div class="steps__line" style="top:226px;height:24px"></div>
        <svg class="steps__icon" style="top:246px"><use href="#i-calc"/></svg>
        <div class="steps__num" style="top:274px">3</div><div class="steps__text" style="top:280px">Bewertung<br>erhalten</div>
        <div class="steps__line" style="top:305px;height:24px"></div>
        <svg class="steps__icon" style="top:324px"><use href="#i-truck"/></svg>
        <div class="steps__num" style="top:352px">4</div><div class="steps__text" style="top:358px">Auszahlung<br>direkt auf Ihr Konto</div>
        <a class="btn btn--gold steps__btn">Versandtasche bestellen</a>
      </div>
    </div>

    <div class="eyebrow" style="left:8px;top:1284px;font-size:2.8px">Familienunternehmen mit Tradition</div>
    <div class="serif abs" style="left:8px;top:1291px;font-size:7.2px">Über <span class="gold">100 Jahre</span><br>Expertise in Gold</div>
    <p class="copy" style="left:8px;top:1315px;width:108px;font-size:2.7px;line-height:1.6">Lorem ipsum dolor sit amet, consetetur sadipscing elitr, sed diam nonumy eirmod tempor invidunt ut labore et dolore magna aliquyam erat, sed diam voluptua. At vero sed diam nonumy eirmod tempor invidunt ut labore.</p>
    <div class="link-u" style="left:8px;top:1352px;font-size:2.7px">MEHR ÜBER UNS ERFAHREN</div>
    <div class="photo photo--expert" style="left:8px;top:1375px;width:109px;height:94px" role="img" aria-label="Foto: Goldexperte prüft Schmuck mit Lupe"></div>

    <div class="eyebrow" style="left:0;width:125px;text-align:center;top:1488px;font-size:2.8px">Kundenstimmen</div>
    <div class="serif abs" style="left:0;width:125px;text-align:center;top:1495px;font-size:7px">Warum uns unsere<br>Kunden vertrauen</div>
    <div class="review" style="left:10px;top:1534px;width:106px;height:100px">
      <div class="review__stars" style="margin-top:9px;font-size:4px">★★★★★</div>
      <p class="review__text" style="margin:4px 10px 0;font-size:3.3px">Meine Erfahrung war einfach nur super. Total nettes Team, schneller Versand. Sehr zuverlässig. Ich bin total happy mit meinem tollen Armband. Dazu war es wundervoll verpackt mit einer kleinen persönlichen Nachricht. Ich bedanke mich!</p>
      <div class="review__name" style="margin-top:8px;font-size:2.6px">Lena Hofer</div>
    </div>
    <div class="review-badge" style="left:12px;top:1524px;width:20px;height:20px" role="img" aria-label="Siegel Kundenbewertungen"></div>
    <div class="arrow" style="left:8px;top:1578px;width:7px;height:7px"><svg width="4" height="4" style="stroke-width:1"><path d="M3 0L1 2l2 2"/></svg></div>
    <div class="arrow" style="left:110px;top:1578px;width:7px;height:7px"><svg width="4" height="4" style="stroke-width:1"><path d="M1 0l2 2-2 2"/></svg></div>

    <div class="cta" style="top:1664px;height:102px">
      <div class="cta__title" style="top:14px;font-size:7px">Wir machen Ihr<br>Gold zu Geld.</div>
      <a class="btn btn--dark" style="left:20px;top:45px;width:84px;height:13px;font-size:2.8px">Jetzt Höchstpreise sichern</a>
      <a class="btn btn--outline" style="left:20px;top:70px;width:84px;height:13px;font-size:2.8px">Versandtasche bestellen</a>
    </div>

    <div class="acc-row" style="top:1768px;height:17px"><span>Kontakt</span><span>+</span></div>
    <div class="acc-row" style="top:1785px;height:17px"><span>Service</span><span>+</span></div>
    <div class="acc-row" style="top:1802px;height:17px"><span>Informationen</span><span>+</span></div>
    <div class="acc-row" style="top:1819px;height:17px"><span>Zahlung &amp; Versand</span><span>+</span></div>

    <div class="foot-bottom" style="top:1844px;height:82px;font-size:3px;line-height:1.55">
      <div style="margin-top:8px;display:flex;justify-content:center;gap:4px"><span class="social social--blue" style="width:9px;height:9px"></span><span class="social social--green" style="width:9px;height:9px"></span></div>
      <div style="margin-top:6px">Kontakt | Über uns | AGB | Impressum |<br>Datenschutz</div>
      <div style="margin-top:2px;padding:0 6px">* Bei den veröffentlichten Ankaufspreisen handelt es sich um Nettopreise.</div>
      <div style="margin-top:8px">© 2022 flinkmetall.de - All Rights Reserved. Theme by Formwerk</div>
    </div>
    <div class="to-top" style="left:103px;top:1890px;width:12px;height:12px;background:#ccc"></div>
  </section>
</div>
</body>
</html>
```